Flyer für Beratung rund um den Computer
Zielgruppe
Hauptsächlich: Beratung rund um den Computer, individuelle Schulungen, technische Hilfe . Aber auch: Einführung in die Programmierung, Webseitenerstellung etc. Zielgruppe sind Privatpersonen, gerne auch ältere Personen, alle die sich unsicher im Umgang mit Computern fühlen und freundliche, geduldige Hilfe suchen.
Aufgabenstellung
Da meine Zielgruppe eher keine Computerfreaks sind, sollte der Flyer nicht zu technisch aussehen, sondern für Hilfesuchende ansprechend und freundlich wirken.

```html
<!DOCTYPE html>
<html lang="de">
<head>
<meta charset="utf-8">
<title>Flyer – PC ganz entspannt</title>
<link href="https://fonts.googleapis.com/css2?family=Anton&family=Poppins:wght@400;500;600;700&display=swap" rel="stylesheet">
<style>
  :root{
    --navy:#1f2f6e;
    --navy-text:#1d2c74;
    --blue:#0a8ccc;
    --sky:#1c8fd6;
    --cyan:#55c6e4;
    --tick:#1a8fd0;
    --ink:#2a2a2a;
    --paper:#ffffff;
    --backdrop:#ecebe8;
  }
  *{margin:0;padding:0;box-sizing:border-box}
  html,body{width:1200px;height:1117px;overflow:hidden;background:var(--backdrop)}
  body{position:relative;font-family:"Poppins",sans-serif}
  .flyer{
    position:absolute;left:219px;top:20px;width:1106px;height:1565px;
    background:var(--paper);transform:scale(0.6882);transform-origin:0 0;overflow:hidden;
    box-shadow:0 6px 24px rgba(0,0,0,.18);
  }
  .abs{position:absolute}
  .headline{
    left:95px;top:48px;font-family:"Anton",sans-serif;font-size:82px;line-height:88px;
    font-weight:400;color:var(--navy-text);white-space:nowrap;
  }
  .headline span{display:block}
  .headline .accent{color:var(--sky)}
  .hero-art{left:0;top:0;width:1106px;height:365px}
  .badge{
    left:660px;top:260px;width:330px;height:330px;border-radius:50%;background:var(--navy);
    display:flex;align-items:center;justify-content:center;text-align:center;
    color:#bfe9f7;font-weight:600;font-size:34px;line-height:42px;letter-spacing:2px;
  }
  .dots{
    left:1000px;top:385px;width:100px;height:190px;
    background:radial-gradient(ellipse at right center,rgba(10,140,204,.75),rgba(10,140,204,0) 75%);
  }
  .intro-frame{
    left:52px;top:357px;width:640px;height:260px;
    border-top:4px solid var(--navy);border-left:4px solid var(--navy);border-top-left-radius:26px;
  }
  .intro{
    left:96px;top:390px;width:540px;font-size:20.5px;font-weight:600;line-height:26.2px;color:var(--navy-text);
  }
  .topic-band{
    left:0;top:607px;width:1106px;height:50px;background:var(--blue);color:#fff;
    font-weight:700;font-size:22px;line-height:50px;text-align:center;
  }
  .questions{left:96px;top:676px;width:960px;list-style:none;font-size:17px;color:var(--ink);line-height:22px}
  .questions li{position:relative;padding-left:30px;margin-bottom:21px}
  .questions li svg{position:absolute;left:0;top:3px}
  .cta{left:0;top:838px;width:1106px;text-align:center;font-weight:700;font-size:24px;color:var(--navy-text)}
  .more-block{left:43px;top:908px;width:1019px;height:237px;background:var(--blue)}
  .more-text{
    left:90px;top:933px;width:926px;text-align:center;color:#fff;font-weight:600;font-size:20px;line-height:25px;
  }
  .navy-band{left:0;top:1027px;width:1106px;height:363px;background:var(--navy)}
  .services{left:89px;top:1044px;width:927px;height:391px;background:var(--navy)}
  .card{position:absolute;width:442px;height:174px;border:2.5px solid var(--cyan);color:#fff;padding:14px 26px}
  .card h3{font-size:21px;font-weight:600;line-height:30px}
  .card ul{list-style:none;font-size:18px;line-height:24.5px}
  .card li{position:relative;padding-left:28px}
  .card li svg{position:absolute;left:0;top:5px}
  .card .cols{display:flex;gap:32px}
  .c1{left:104px;top:1059px}
  .c2{left:560px;top:1059px}
  .c3{left:104px;top:1246px}
  .c4{left:560px;top:1246px;padding-top:34px}
  .phone{left:88px;top:1466px;display:flex;align-items:center;gap:12px}
  .phone-number{font-weight:700;font-size:54px;color:var(--navy-text);letter-spacing:1px}
  .divider{left:573px;top:1470px;width:2px;height:55px;background:var(--navy-text)}
  .contacts{left:592px;top:1468px;font-weight:700;font-size:19px;color:var(--navy-text);line-height:29px}
  .contacts div{display:flex;align-items:center;gap:10px}
</style>
</head>
<body>
<main class="flyer">
  <svg class="abs hero-art" viewBox="0 0 1106 365" role="img" aria-label="Foto: Laptop, Tablet und Smartphone mit Kaffeetasse auf einem Holztisch">
    <defs>
      <clipPath id="heroClip"><circle cx="1000" cy="130" r="390"/></clipPath>
      <linearGradient id="heroTone" x1="0" y1="0" x2="1" y2="1">
        <stop offset="0" stop-color="#3b4048"/>
        <stop offset=".55" stop-color="#8a7d6e"/>
        <stop offset="1" stop-color="#6b4a32"/>
      </linearGradient>
    </defs>
    <path d="M640 0 A390 390 0 0 0 700 360" fill="none" stroke="var(--sky)" stroke-width="10" transform="translate(-26 0)"/>
    <rect x="0" y="0" width="1106" height="360" fill="url(#heroTone)" clip-path="url(#heroClip)"/>
  </svg>

  <h1 class="abs headline"><span>Computer -</span><span>Alles, Nur Kein</span><span class="accent">Hexenwissen</span></h1>

  <div class="abs intro-frame"></div>
  <p class="abs intro">Ganz egal, was Sie im Zusammenhang mit Ihrem Rechner umtreibt - ob Sie sich manchmal einfach etwas unsicher fühlen, mit einer Anwendung nicht zurecht kommen oder Ihr Rechner nicht so reagiert, wie er sollte - mein Ziel ist es, dass Sie sich im Umgang mit Ihrem Computer sicher fühlen und Freude daran haben.</p>

  <div class="abs dots" role="img" aria-label="Dekoratives Punktraster"></div>
  <div class="abs badge">PC GANZ<br>ENTSPANNT</div>

  <div class="abs topic-band">Auch viele andere Themen werfen immer wieder Fragen auf:</div>

  <ul class="abs questions">
    <li><svg width="18" height="14" viewBox="0 0 18 14"><path d="M1.5 7.5l5 5L16.5 1.5" fill="none" stroke="var(--tick)" stroke-width="3.4"/></svg>Ich brauche einen neuen Rechner - wie finde ich heraus, was ich wirklich brauche?</li>
    <li><svg width="18" height="14" viewBox="0 0 18 14"><path d="M1.5 7.5l5 5L16.5 1.5" fill="none" stroke="var(--tick)" stroke-width="3.4"/></svg>Wie organisiere ich meinen Rechner damit ich alles schnell wiederfinde?</li>
    <li><svg width="18" height="14" viewBox="0 0 18 14"><path d="M1.5 7.5l5 5L16.5 1.5" fill="none" stroke="var(--tick)" stroke-width="3.4"/></svg>Wie bekomme ich die Fotos von meiner Kamera / meinem Smartphone auf meinen Rechner?<br>,und so weiter.</li>
  </ul>

  <p class="abs cta">Legen Sie los - egal wie klein oder groß Ihre Frage ist - ich helfe gerne!</p>

  <div class="abs more-block"></div>
  <p class="abs more-text">Und für alle, die etwas mehr wissen wollen - z.B. wie das mit dem Programmieren eigentlich funktioniert, wie eine Webseite entsteht, wofür ein Router benötigt wird, wie nutze ich eine KI, usw. - ich gebe gerne eine Einführung dazu.</p>

  <div class="abs navy-band"></div>
  <div class="abs services"></div>

  <section class="card c1">
    <h3>Beratung rund um Ihren Rechner:</h3>
    <div class="cols">
      <ul>
        <li><svg width="16" height="12" viewBox="0 0 18 14"><path d="M1.5 7.5l5 5L16.5 1.5" fill="none" stroke="var(--cyan)" stroke-width="3.4"/></svg>Kauf</li>
        <li><svg width="16" height="12" viewBox="0 0 18 14"><path d="M1.5 7.5l5 5L16.5 1.5" fill="none" stroke="var(--cyan)" stroke-width="3.4"/></svg>Organisation</li>
        <li><svg width="16" height="12" viewBox="0 0 18 14"><path d="M1.5 7.5l5 5L16.5 1.5" fill="none" stroke="var(--cyan)" stroke-width="3.4"/></svg>Anwendungen</li>
        <li><svg width="16" height="12" viewBox="0 0 18 14"><path d="M1.5 7.5l5 5L16.5 1.5" fill="none" stroke="var(--cyan)" stroke-width="3.4"/></svg>Optimierung</li>
      </ul>
      <ul>
        <li><svg width="16" height="12" viewBox="0 0 18 14"><path d="M1.5 7.5l5 5L16.5 1.5" fill="none" stroke="var(--cyan)" stroke-width="3.4"/></svg>Internet</li>
        <li><svg width="16" height="12" viewBox="0 0 18 14"><path d="M1.5 7.5l5 5L16.5 1.5" fill="none" stroke="var(--cyan)" stroke-width="3.4"/></svg>Datensicherung</li>
        <li><svg width="16" height="12" viewBox="0 0 18 14"><path d="M1.5 7.5l5 5L16.5 1.5" fill="none" stroke="var(--cyan)" stroke-width="3.4"/></svg>... und vieles mehr</li>
      </ul>
    </div>
  </section>

  <section class="card c2">
    <h3>Technische Hilfe:</h3>
    <ul>
      <li><svg width="16" height="12" viewBox="0 0 18 14"><path d="M1.5 7.5l5 5L16.5 1.5" fill="none" stroke="var(--cyan)" stroke-width="3.4"/></svg>Anschluß von Peripheriegeräten</li>
      <li><svg width="16" height="12" viewBox="0 0 18 14"><path d="M1.5 7.5l5 5L16.5 1.5" fill="none" stroke="var(--cyan)" stroke-width="3.4"/></svg>Einbinden von Peripheriegeräten ins Netzwerk / WLAN</li>
      <li><svg width="16" height="12" viewBox="0 0 18 14"><path d="M1.5 7.5l5 5L16.5 1.5" fill="none" stroke="var(--cyan)" stroke-width="3.4"/></svg>Kleinere Reparaturen</li>
      <li><svg width="16" height="12" viewBox="0 0 18 14"><path d="M1.5 7.5l5 5L16.5 1.5" fill="none" stroke="var(--cyan)" stroke-width="3.4"/></svg>oder: was brauchen Sie?</li>
    </ul>
  </section>

  <section class="card c3">
    <h3>Für alle, die mehr wollen:</h3>
    <ul>
      <li><svg width="16" height="12" viewBox="0 0 18 14"><path d="M1.5 7.5l5 5L16.5 1.5" fill="none" stroke="var(--cyan)" stroke-width="3.4"/></svg>Einführung in die Programmierung</li>
      <li><svg width="16" height="12" viewBox="0 0 18 14"><path d="M1.5 7.5l5 5L16.5 1.5" fill="none" stroke="var(--cyan)" stroke-width="3.4"/></svg>Erstellen einer Website</li>
      <li><svg width="16" height="12" viewBox="0 0 18 14"><path d="M1.5 7.5l5 5L16.5 1.5" fill="none" stroke="var(--cyan)" stroke-width="3.4"/></svg>Wie komme ich einer KI näher?</li>
      <li><svg width="16" height="12" viewBox="0 0 18 14"><path d="M1.5 7.5l5 5L16.5 1.5" fill="none" stroke="var(--cyan)" stroke-width="3.4"/></svg>oder: was interessiert Sie?</li>
    </ul>
  </section>

  <section class="card c4">
    <h3>Individuelle Schulungen:</h3>
    <ul>
      <li><svg width="16" height="12" viewBox="0 0 18 14"><path d="M1.5 7.5l5 5L16.5 1.5" fill="none" stroke="var(--cyan)" stroke-width="3.4"/></svg>allgemeiner Umgang mit dem Rechner</li>
      <li><svg width="16" height="12" viewBox="0 0 18 14"><path d="M1.5 7.5l5 5L16.5 1.5" fill="none" stroke="var(--cyan)" stroke-width="3.4"/></svg>Nutzung bestimmter Anwendungen</li>
      <li><svg width="16" height="12" viewBox="0 0 18 14"><path d="M1.5 7.5l5 5L16.5 1.5" fill="none" stroke="var(--cyan)" stroke-width="3.4"/></svg>oder: was wünschen Sie sich?</li>
    </ul>
  </section>

  <div class="abs phone">
    <svg width="46" height="46" viewBox="0 0 46 46" aria-hidden="true">
      <circle cx="23" cy="23" r="23" fill="var(--sky)"/>
      <path d="M15 12c2-1 3 0 4 2l2 4c.5 1 0 2-1 3l-1.5 1.2c1.4 3 3.4 5 6.3 6.3L26 27c1-1 2-1.5 3-1l4 2c2 1 3 2 2 4-1.5 3-4 4-7 3-7-2-12-7-14-14-1-3 0-5.5 3-7z" fill="#fff"/>
    </svg>
    <span class="phone-number">0157 218 6603</span>
  </div>
  <div class="abs divider"></div>
  <div class="abs contacts">
    <div><svg width="18" height="18" viewBox="0 0 18 18" aria-hidden="true"><circle cx="9" cy="9" r="9" fill="var(--sky)"/><rect x="4.5" y="5.8" width="9" height="6.4" fill="none" stroke="#fff" stroke-width="1.3"/><path d="M4.5 6l4.5 3.5L13.5 6" fill="none" stroke="#fff" stroke-width="1.3"/></svg>mira@pc-ganz-entspannt.de</div>
    <div><svg width="18" height="18" viewBox="0 0 18 18" aria-hidden="true"><circle cx="9" cy="9" r="9" fill="var(--sky)"/><circle cx="9" cy="9" r="4.6" fill="none" stroke="#fff" stroke-width="1.2"/><path d="M4.4 9h9.2M9 4.4c-2.4 2.6-2.4 6.6 0 9.2M9 4.4c2.4 2.6 2.4 6.6 0 9.2" fill="none" stroke="#fff" stroke-width="1.1"/></svg>www.pc-ganz-entspannt.de</div>
  </div>
</main>
</body>
</html>
```